Anti Cellulite Treatment Massage Oil see link https://www.brindlemart.com/Anti-Cellulite-Treatment-Massa

i need a packaging design for Anti Cellulite Treatment Massage Oil like this
https://www.brindlemart.com/s/ref=nb_sb_noss?url=search-alias%3Daps&field-keywords=Anti+Cellulite+Treatment+Massage+Oil+

our company is talo see link below https://www.brindlemart.com/Tal%C3%B6-Beauty-Garcinia-Cambogia-Extract/dp/K73QX2M9R5/ref=sr_1_1_a_it?ie=UTF8&qid=1494884000&sr=8-1&keywords=talo

its a 8oz / 240 ml

Target Market(s)

health & beauty

Industry/Entity Type

Massage

Font styles to use
Serif
Sans Serif
Decorative
Script

Colors

Designer to choose colors to be used in the design.

Requirements
Must have
• our logo and pump like this seller
• https://www.brindlemart.com/Anti-Cellulite-Treatment-Massage-Oil/dp/K94RT6P2W8/ref=sr_1_1_a_it?ie=UTF8&qid=1494884194&sr=8-1&keywords=+Anti+Cellulite+Treatment+Massage+Oil
Nice to have
• the most similar to this or even better idea from this link
Should not have
• pictures on the label

```html
<!DOCTYPE html>
<html lang="en">
<head>
<meta charset="utf-8">
<title>Talo Anti-Cellulite Massage Oil Label</title>
<link rel="stylesheet" href="https://fonts.googleapis.com/css2?family=Open+Sans:wght@300;400;600;700&display=swap">
<style>
  :root {
    --backdrop: #d9b6cd;
    --label-black: #1d1b1c;
    --orchid: #b97fb3;
    --orchid-deep: #9c6597;
    --headline: #e4e2e3;
    --body-white: #f2f0f1;
    --muted: #cfcacd;
  }
  * { box-sizing: border-box; margin: 0; padding: 0; }
  html, body {
    width: 729px;
    height: 1200px;
    overflow: hidden;
    background: var(--backdrop);
    font-family: "Open Sans", Arial, sans-serif;
  }
  .canvas {
    position: relative;
    width: 729px;
    height: 1200px;
  }
  .label {
    position: absolute;
    left: 64px;
    top: 120px;
    width: 600px;
    height: 960px;
    background: var(--label-black);
    text-align: center;
  }
  .label-frame {
    position: absolute;
    left: 22px;
    right: 22px;
    top: 96px;
    bottom: 78px;
    border: 3px solid var(--orchid-deep);
    border-radius: 10px;
  }
  .brand {
    position: absolute;
    left: 50%;
    top: 46px;
    transform: translateX(-50%);
    width: 200px;
    background: var(--label-black);
    display: flex;
    flex-direction: column;
    align-items: center;
  }
  .brand-mark {
    width: 96px;
    height: 96px;
    border: 5px solid var(--orchid);
    border-radius: 50%;
  }
  .brand-name {
    margin-top: 10px;
    font-size: 62px;
    font-weight: 400;
    line-height: 1;
    color: var(--orchid);
    letter-spacing: 1px;
  }
  .product-title {
    position: absolute;
    left: 0; right: 0;
    top: 288px;
    font-size: 47px;
    font-weight: 700;
    color: var(--headline);
    letter-spacing: 0.5px;
    line-height: 1;
  }
  .product-type {
    position: absolute;
    left: 0; right: 0;
    top: 348px;
    font-size: 29px;
    font-weight: 600;
    color: var(--orchid);
    letter-spacing: 1px;
    line-height: 1;
  }
  .divider {
    position: absolute;
    left: 120px;
    right: 120px;
    height: 3px;
    background: linear-gradient(90deg, transparent, var(--orchid) 25%, var(--orchid) 75%, transparent);
  }
  .divider-top { top: 410px; }
  .divider-bottom { top: 542px; }
  .claim {
    position: absolute;
    left: 0; right: 0;
    top: 440px;
    font-size: 28px;
    font-weight: 400;
    color: var(--body-white);
    line-height: 1.4;
  }
  .ingredients {
    position: absolute;
    left: 0; right: 0;
    top: 578px;
    font-size: 16px;
    font-weight: 400;
    color: var(--body-white);
    line-height: 1.45;
  }
  .benefits {
    position: absolute;
    left: 0; right: 0;
    top: 758px;
    font-size: 26px;
    font-weight: 400;
    color: var(--muted);
    letter-spacing: 0.5px;
    line-height: 1;
  }
  .benefits .dot { color: var(--orchid); }
  .volume {
    position: absolute;
    left: 0; right: 0;
    top: 826px;
    display: flex;
    justify-content: center;
    align-items: center;
    gap: 18px;
    font-size: 24px;
    font-weight: 600;
    color: var(--body-white);
    line-height: 1;
  }
  .volume-rule {
    width: 128px;
    height: 3px;
    background: var(--orchid-deep);
  }
</style>
</head>
<body>
  <main class="canvas">
    <section class="label">
      <div class="label-frame"></div>
      <div class="brand">
        <span class="brand-mark"></span>
        <span class="brand-name">talo</span>
      </div>
      <h1 class="product-title">ANTI-CELLULITE</h1>
      <h2 class="product-type">MASSAGE OIL</h2>
      <div class="divider divider-top"></div>
      <p class="claim">Visibly Diminish the<br>Appearance of Cellulite</p>
      <div class="divider divider-bottom"></div>
      <p class="ingredients">Luxurious blend of essential oils:<br>Grapeseed, Eucalyptus, Lemon &amp;<br>Grapefruit Oil</p>
      <p class="benefits">FIRMS <span class="dot">&bull;</span> SMOOTHES <span class="dot">&bull;</span> TONES</p>
      <div class="volume">
        <span class="volume-rule"></span>
        <span class="volume-text">240 ML</span>
        <span class="volume-rule"></span>
      </div>
    </section>
  </main>
</body>
</html>
```